LOGO DESIGN: Construction Related Service Business

We require a logo for our business Tovar Services. We are a construction related business offering a range of services including machine services for groundworks (digging trenches, soak wells, preparing land for construction etc), demolition and truck haulage from demolition sites.
We would like our logo to be predominately text, but may include abstract graphics. The colour scheme should be mainly a mid bright blue and overall be quite 'clean'.

Industry/Entity Type

Construction

Contact Information for Business Card

Dale Morrow
Ph:041 592 3068
tovarservices@quillnet.com.au

Colors
0456a3

```html
<!DOCTYPE html>
<html lang="en">
<head>
<meta charset="utf-8">
<title>Tovar Services – Business Card</title>
<link rel="stylesheet" href="https://fonts.googleapis.com/css2?family=Source+Sans+3:wght@400;700&display=swap">
<style>
  :root {
    --backdrop: #d9dadc;
    --card: #ffffff;
    --brand-blue: #0d56a6;
    --band-top: #4a95d3;
    --band-bottom: #c6ddf2;
    --pattern-soft: #f1f5fb;
    --ink: #1a1a1a;
    --icon-red: #b3262b;
    --edge: #2a2a2a;
  }
  * { margin: 0; padding: 0; box-sizing: border-box; }
  html, body {
    width: 1200px; height: 1200px; overflow: hidden;
    background: var(--backdrop);
    font-family: "Source Sans 3", Arial, sans-serif;
  }
  .business-card {
    position: absolute;
    left: 108px; top: 304px;
    width: 980px; height: 592px;
  }
  .card-art { position: absolute; inset: 0; }
  .brand {
    position: absolute; left: 106px; top: 76px;
    display: flex; align-items: center; gap: 16px;
  }
  .brand-mark {
    width: 80px; height: 80px; background: var(--brand-blue);
  }
  .brand-name {
    color: var(--brand-blue); font-weight: 700;
    font-size: 50px; line-height: 42px;
  }
  .contact {
    position: absolute; right: 66px; top: 292px;
    text-align: right; color: var(--ink);
  }
  .contact-name {
    color: var(--brand-blue); font-weight: 700;
    font-size: 31px; margin-right: 38px; margin-bottom: 16px;
  }
  .contact-line {
    display: flex; justify-content: flex-end; align-items: center;
    gap: 14px; font-size: 24px; line-height: 29px;
  }
  .contact-icon { width: 24px; height: 20px; }
</style>
</head>
<body>
  <div class="business-card">
    <svg class="card-art" width="980" height="592" viewBox="0 0 980 592">
      <defs>
        <clipPath id="card-shape">
          <path d="M0 0 H920 A60 60 0 0 1 980 60 V592 H60 A60 60 0 0 1 0 532 Z"/>
        </clipPath>
        <linearGradient id="band-fade" x1="0" y1="0" x2="0" y2="1">
          <stop offset="0" stop-color="var(--band-top)"/>
          <stop offset="1" stop-color="var(--band-bottom)"/>
        </linearGradient>
        <linearGradient id="pattern-fade" x1="0" y1="0" x2="1" y2="1">
          <stop offset="0" stop-color="var(--card)"/>
          <stop offset="0.5" stop-color="var(--pattern-soft)"/>
          <stop offset="1" stop-color="var(--card)"/>
        </linearGradient>
      </defs>
      <g clip-path="url(#card-shape)">
        <rect width="980" height="592" fill="var(--card)"/>
        <rect class="pattern-area" x="0" y="0" width="980" height="512" fill="url(#pattern-fade)"
              role="img" aria-label="Faint decorative pipe-bend background pattern"/>
        <path class="wave" d="M264 512 C340 500 420 492 500 492 H980 V512 Z" fill="var(--brand-blue)"/>
        <rect class="base-band" x="0" y="512" width="980" height="80" fill="url(#band-fade)"/>
      </g>
      <path d="M0.5 0.5 H920 A59.5 59.5 0 0 1 979.5 60 V591.5 H60 A59.5 59.5 0 0 1 0.5 532 Z"
            fill="none" stroke="var(--edge)" stroke-width="1"/>
    </svg>

    <div class="brand">
      <div class="brand-mark"></div>
      <div class="brand-name">Tovar<br>Services</div>
    </div>

    <div class="contact">
      <div class="contact-name">Dale Morrow</div>
      <div class="contact-line">
        <span>041 592 3068</span>
        <svg class="contact-icon" viewBox="0 0 24 20" aria-label="Phone">
          <path d="M5 4 C9 0 18 0 22 4 L19 8 L16 6 L16 4 C13 3 10 3 8 4 L8 6 L5 8 Z" fill="var(--icon-red)" transform="rotate(-35 12 10)"/>
        </svg>
      </div>
      <div class="contact-line">
        <span>tovarservices@quillnet.com.au</span>
        <svg class="contact-icon" viewBox="0 0 24 20" aria-label="Email">
          <rect x="1" y="4" width="22" height="15" fill="var(--icon-red)"/>
          <path d="M1 4 L12 12 L23 4" fill="none" stroke="#fff" stroke-width="1.5"/>
          <path d="M1 19 L9 10 M23 19 L15 10" stroke="#fff" stroke-width="1"/>
        </svg>
      </div>
    </div>
  </div>
</body>
</html>
```